Business Card Design Project for Investment Fund

Veloria Capital Management is an emerging wealth management firm based in New Jersey. It offers superior investment returns to high net worth individuals and institutions by finding undervalued assets.
We recently selected a company logo which was inspired by the Tucana constellation. Beta Tucanae is a group of six stars, containing star cluster 47 Tucanae, rated the second brightest object in the sky.
Now we need a business card design. Since we are an investment firm, the design should project a sense of stability, growth and professionalism. The owner is interested in something simple yet striking, which of course is consistent with the logo.
Wealthy individuals, probably middle aged or older, in the US
Investment

```html
<!DOCTYPE html>
<html lang="en">
<head>
<meta charset="utf-8">
<title>Veloria Capital Management — Business Card</title>
<link rel="stylesheet" href="https://fonts.googleapis.com/css2?family=Source+Sans+3:wght@400;600&display=swap">
<style>
  :root {
    --backdrop: #ebe6e0;
    --card-white: #ffffff;
    --card-grey: #666666;
    --navy: #242a6b;
    --slate: #2f3a3d;
    --text-grey: #5c5f61;
    --ink: #1f2326;
    --brand-blue: #2b3a9c;
    --rule: #8a8d8f;
    --shadow: rgba(0, 0, 0, 0.18);
  }
  * { box-sizing: border-box; margin: 0; padding: 0; }
  html, body {
    width: 1200px; height: 1024px; overflow: hidden;
    background: var(--backdrop);
    font-family: "Source Sans 3", "Myriad Pro", sans-serif;
  }
  .canvas { position: relative; width: 1200px; height: 1024px; }

  .card {
    position: absolute;
    width: 780px; height: 446px;
    border-radius: 40px;
    box-shadow: 0 8px 22px var(--shadow);
  }

  /* Front */
  .card--front { left: 110px; top: 46px; background: var(--card-white); }
  .brand-block {
    position: absolute; left: 60px; top: 96px; width: 300px;
    display: flex; flex-direction: column; align-items: center;
  }
  .brand-square {
    width: 140px; height: 140px; border-radius: 22px;
    background: linear-gradient(160deg, #3346b4, var(--brand-blue) 55%, #1d2672);
  }
  .brand-name {
    margin-top: 22px; text-align: center;
    font-weight: 600; color: var(--slate);
    font-size: 34px; line-height: 1.05; letter-spacing: 0.5px;
  }
  .divider {
    position: absolute; left: 392px; top: 90px; width: 1.5px; height: 262px;
    background: var(--rule);
  }
  .contact {
    position: absolute; left: 430px; top: 92px; color: var(--ink);
  }
  .contact__name { font-size: 30px; font-weight: 600; color: var(--navy); line-height: 1.1; }
  .contact__title { font-size: 21px; color: var(--text-grey); letter-spacing: 0.8px; margin-top: 2px; }
  .contact__address { font-size: 22px; line-height: 1.3; margin-top: 30px; }
  .contact__list { list-style: none; margin-top: 16px; }
  .contact__item {
    display: flex; align-items: center; gap: 8px;
    font-size: 22px; line-height: 1.6;
  }
  .contact__icon { width: 20px; height: 20px; flex: none; }

  /* Back */
  .card--back { left: 310px; top: 532px; background: var(--card-grey); color: #ffffff; }
  .back-name {
    position: absolute; left: 0; right: 0; top: 90px; text-align: center;
    font-weight: 600; font-size: 64px; line-height: 1.05; letter-spacing: 1px;
  }
  .back-web {
    position: absolute; left: 0; right: 0; top: 318px; text-align: center;
    font-size: 22px; letter-spacing: 2px;
  }
</style>
</head>
<body>
<main class="canvas">

  <section class="card card--front" aria-label="Business card front">
    <div class="brand-block">
      <div class="brand-square"></div>
      <div class="brand-name">Veloria<br>Capital Management</div>
    </div>

    <div class="divider"></div>

    <div class="contact">
      <p class="contact__name">Adrian Hale</p>
      <p class="contact__title">Marketing Manager</p>
      <p class="contact__address">48 Harbor Ave.<br>Newark, NJ 07102</p>
      <ul class="contact__list">
        <li class="contact__item">
          <svg class="contact__icon" viewBox="0 0 20 20" aria-hidden="true">
            <circle cx="10" cy="10" r="8.5" fill="none" stroke="var(--navy)" stroke-width="1.5"/>
            <path d="M7 5.5 L9 8 L8 9.5 Q9 11.5 10.5 12 L12 11 L14.5 13 L13 14.5 Q8.5 14 5.5 8 Z" fill="var(--navy)"/>
          </svg>
          973-555-0142
        </li>
        <li class="contact__item">
          <svg class="contact__icon" viewBox="0 0 20 20" aria-hidden="true">
            <rect x="2" y="5" width="16" height="11" rx="1.5" fill="var(--navy)"/>
            <path d="M2.5 5.5 L10 11 L17.5 5.5" fill="none" stroke="#ffffff" stroke-width="1.3"/>
          </svg>
          ahale@veloriacapmgmt.com
        </li>
        <li class="contact__item">
          <svg class="contact__icon" viewBox="0 0 20 20" aria-hidden="true">
            <g fill="none" stroke="var(--navy)" stroke-width="1.3">
              <circle cx="10" cy="10" r="8"/>
              <ellipse cx="10" cy="10" rx="3.5" ry="8"/>
              <line x1="2" y1="10" x2="18" y2="10"/>
              <line x1="3.5" y1="6" x2="16.5" y2="6"/>
              <line x1="3.5" y1="14" x2="16.5" y2="14"/>
            </g>
          </svg>
          www.veloriacapmgmt.com
        </li>
      </ul>
    </div>
  </section>

  <section class="card card--back" aria-label="Business card back">
    <div class="back-name">Veloria<br>Capital Management</div>
    <p class="back-web">www.veloriacapmgmt.com</p>
  </section>

</main>
</body>
</html>
```